Business Card for new Architectural Firm

I intend to practice in a rural mountain community in upstate NY, focusing on residential and light commercial projects, including second home / vacation properties. I wish to convey a feeling of rural outdoorsy modernity.

Color is important - bold and urbane. Secondary or tertiary colors preferred.

Font is important, idiosyncratic is ok

Optionally, I may choose to use the name Brackenfold Studio. If used as part of your design, all of the Must Haves are still required.

Images uploaded are logos I like

Industry/Entity Type

Residential

Contact Information for Business Card

Lionel Harwicke
Architect (This word should stand alone or be associated with my name - not license number)
NY License No. 052816
lionel@designlhq.com
607 382 9154

Font styles to use
Sans Serif
Decorative

Requirements
Must have
• Whatever files I need to best utilize your design
• PDF
• JPG
• EPS
• Vectorwhatsit
Nice to have
• Logo or element that can be incorporated into other print material.
• Could be a font based card
Should not have
• no clip art
• No templates
• no floor plans
• no building photographs

```html
<!DOCTYPE html>
<html lang="en">
<head>
<meta charset="utf-8">
<title>Lionel Harwicke — Architect business card</title>
<link rel="stylesheet" href="https://fonts.googleapis.com/css2?family=Montserrat:wght@300;400&display=swap">
<style>
  :root {
    --backdrop: #d9d9d9;
    --card-light: #f4f4f2;
    --card-dark: #0a0a0a;
    --accent: #f0b82a;
    --ink-dark: #3a3a3a;
    --ink-light: #d6d6d6;
    --muted-dark: #6a6a6a;
    --muted-light: #9a9a9a;
  }
  * { box-sizing: border-box; margin: 0; padding: 0; }
  html, body {
    width: 1200px;
    height: 1000px;
    overflow: hidden;
    background: var(--backdrop);
    font-family: "Montserrat", "Helvetica Neue", Arial, sans-serif;
  }
  .canvas {
    position: relative;
    width: 1200px;
    height: 1000px;
  }
  .card {
    position: absolute;
    left: 320px;
    width: 560px;
    height: 320px;
    display: flex;
    flex-direction: column;
    align-items: center;
    padding-top: 42px;
    box-shadow: 0 6px 18px rgba(0,0,0,0.18);
  }
  .card--light { top: 140px; background: var(--card-light); color: var(--ink-dark); }
  .card--dark  { top: 530px; background: var(--card-dark);  color: var(--ink-light); }

  .brand-square {
    width: 40px;
    height: 40px;
    background: var(--accent);
    margin-bottom: 14px;
  }
  .card__name {
    font-weight: 300;
    font-size: 42px;
    line-height: 1;
    letter-spacing: 0.5px;
  }
  .card__title {
    font-weight: 300;
    font-size: 12px;
    letter-spacing: 11px;
    margin-top: 6px;
    margin-left: 11px;
  }
  .card--light .card__title { color: var(--muted-dark); }
  .card--dark  .card__title { color: var(--muted-light); }

  .contact {
    list-style: none;
    margin-top: 34px;
    text-align: center;
    font-size: 15px;
    font-weight: 400;
    line-height: 1.55;
  }
  .contact .accent { color: var(--accent); }
</style>
</head>
<body>
<main class="canvas">

  <section class="card card--light" aria-label="Business card, light side">
    <div class="brand-square" aria-hidden="true"></div>
    <h1 class="card__name">Lionel Harwicke</h1>
    <p class="card__title">ARCHITECT</p>
    <ul class="contact">
      <li>License No. <span class="accent">052816</span></li>
      <li>607 - 382 - 9154</li>
      <li><span class="accent">lionel@designlhq</span>.com</li>
    </ul>
  </section>

  <section class="card card--dark" aria-label="Business card, dark side">
    <div class="brand-square" aria-hidden="true"></div>
    <h2 class="card__name">Lionel Harwicke</h2>
    <p class="card__title">ARCHITECT</p>
    <ul class="contact">
      <li>License No. <span class="accent">052816</span></li>
      <li>607 - 382 - 9154</li>
      <li><span class="accent">lionel@designlhq</span>.com</li>
    </ul>
  </section>

</main>
</body>
</html>
```